Broadcaster,Conference Host,Facilitator

Looking for a business card and logo to create the Grant Ollerby brand .. Something with a slant towards radio and conference speaking
I like the idea of classic black white or grey but open to suggestions

Target Market(s)

Corporates

Industry/Entity Type

Business

Contact Information for Business Card

Grant Ollerby
Email : Grant.Ollerby@fenmail.co.uk
Mobile : +44 7700 384216
Twitter : @Grantollerby

Font styles to use
Serif
Decorative
Script

Requirements
Must have
• Feel classy and dynamic
Should not have
• Cartoons

```html
<!DOCTYPE html>
<html lang="en">
<head>
<meta charset="utf-8">
<title>Grant Ollerby – Business Card</title>
<link rel="stylesheet" href="https://fonts.googleapis.com/css2?family=Tinos:wght@400;700&family=Great+Vibes&display=swap">
<style>
  :root {
    --backdrop: #2c2d31;
    --card: #050505;
    --ink: #f4f4f4;
    --edge: #1a1a1a;
  }
  * { box-sizing: border-box; margin: 0; padding: 0; }
  html, body {
    width: 1200px;
    height: 900px;
    overflow: hidden;
    background: var(--backdrop);
  }
  .canvas {
    width: 1200px;
    height: 900px;
    display: flex;
    flex-direction: column;
    align-items: center;
    justify-content: center;
    gap: 48px;
  }
  .card {
    width: 660px;
    height: 378px;
    background: var(--card);
    border: 1px solid var(--edge);
    border-radius: 3px;
    box-shadow: 0 14px 30px rgba(0,0,0,0.45);
    position: relative;
    color: var(--ink);
    font-family: "Tinos", "Times New Roman", serif;
  }
  .wordmark {
    display: flex;
    align-items: center;
    gap: 12px;
    font-family: "Tinos", "Times New Roman", serif;
    font-weight: 400;
    color: var(--ink);
    letter-spacing: 0.5px;
    white-space: nowrap;
  }
  .wordmark-dot {
    width: 12px;
    height: 12px;
    border-radius: 50%;
    background: var(--ink);
    flex: none;
  }
  .card-front .wordmark {
    position: absolute;
    left: 50%;
    top: 50%;
    transform: translate(-50%, -50%);
    font-size: 40px;
  }
  .card-back .wordmark {
    position: absolute;
    left: 48px;
    top: 50%;
    transform: translateY(-50%);
    font-size: 38px;
  }
  .contact {
    position: absolute;
    right: 40px;
    top: 50%;
    transform: translateY(-50%);
    width: 260px;
  }
  .contact-name {
    font-family: "Great Vibes", cursive;
    font-size: 30px;
    font-weight: 400;
    margin-bottom: 12px;
    margin-left: 8px;
  }
  .contact-list {
    list-style: none;
    font-size: 14px;
    line-height: 1.45;
    margin-left: 30px;
  }
  .contact-label { font-weight: 700; }
</style>
</head>
<body>
  <main class="canvas">
    <section class="card card-front" aria-label="Card front">
      <div class="wordmark"><span class="wordmark-dot"></span>Grant Ollerby</div>
    </section>

    <section class="card card-back" aria-label="Card back">
      <div class="wordmark"><span class="wordmark-dot"></span>Grant Ollerby</div>
      <div class="contact">
        <p class="contact-name">Grant Ollerby</p>
        <ul class="contact-list">
          <li><span class="contact-label">Email :</span> Grant.Ollerby@fenmail.co.uk</li>
          <li><span class="contact-label">Mobile :</span> +44 7700 384216</li>
          <li><span class="contact-label">Twitter :</span> @Grantollerby</li>
        </ul>
      </div>
    </section>
  </main>
</body>
</html>
```